Meadowlark Pet Business Card

We need a business card designed with two sides to it. I would like the front of the card to be mostly graphic and the back of the card to have the bullet points of our pet food.

I don't have a telephone number for the business yet so just leave a space for a toll free number. (800) xxx-xxxx.

Thanks,

Dale
Updates

Combination Diet
Chicken Diet
Beef Diet
Lamb Diet

Website:  www.meadowlarkpet-example.com

email:  tbrowning@meadowlarkpet-example.com

Direct - 555-xxx-xxxx
Toll Free - xxx-xxx-xxxx

www.meadowlarkpet-example.com

Tom Browning (Example)
Customer Experience Officer

tbrowning@meadowlarkpet-example.com
Direct - (555) xxx-xxxx

Sales Inquiries - (800) xxx-xxxx

All,

Please include the following items on the back of the business card.

Combination Diet
Chicken Diet
Beef Diet
Lamb Diet
 

Thanks,

Dale

All, I will also want a QR code on the front or back of the card that can be scanned by a smart phone with our individual contact information.  Thanks, Dale

Industry/Entity Type

Pet

```html
<!DOCTYPE html>
<html lang="en">
<head>
<meta charset="utf-8">
<title>Meadowlark Pet – Business Card</title>
<link href="https://fonts.googleapis.com/css2?family=Lato:wght@400;700;900&display=swap" rel="stylesheet">
<style>
  :root {
    --page: #e6e6e6;
    --ink: #000000;
    --sun: #ffe100;
    --sun-soft: #f7d21a;
    --amber: #f4a51c;
    --ember: #d9542a;
    --rust: #c9422a;
    --gold-text: #f5d90a;
    --white: #ffffff;
  }
  * { box-sizing: border-box; margin: 0; padding: 0; }
  html, body {
    width: 1200px; height: 1178px; overflow: hidden;
    background: var(--page);
    font-family: "Lato", Arial, sans-serif;
  }
  .card {
    position: absolute; left: 107px; width: 987px; height: 560px;
    overflow: hidden; box-shadow: 0 2px 6px rgba(0,0,0,.25);
  }
  .card-front { top: 24px; background: var(--ember); }
  .card-back { top: 593px; background: var(--ink); }

  .sunset-scene {
    position: absolute; inset: 0 0 182px 0;
    background:
      radial-gradient(circle at 50% 52%, var(--sun) 0 36%, transparent 36.5%),
      radial-gradient(ellipse at 50% 45%, var(--sun-soft) 0%, var(--amber) 30%, var(--ember) 65%, var(--rust) 100%);
  }
  .brand-block {
    position: absolute; left: 337px; top: 22px; width: 310px; height: 158px;
    border: 8px solid var(--ink);
    display: flex; align-items: center; justify-content: center;
    background: rgba(0,0,0,.08);
  }
  .brand-name {
    font-weight: 900; font-size: 40px; color: var(--ink); letter-spacing: -.5px;
  }
  .tagline {
    position: absolute; left: 345px; top: 186px; width: 325px; height: 34px;
    background: var(--ink); color: var(--white);
    font-weight: 900; font-size: 15px; letter-spacing: 1.6px;
    display: flex; align-items: center; justify-content: center;
  }
  .holder {
    position: absolute; left: 0; right: 0; top: 244px; text-align: center; color: var(--ink);
  }
  .holder-name { font-weight: 900; font-size: 37px; line-height: 40px; }
  .holder-title { font-size: 24px; line-height: 30px; }

  .contact-band {
    position: absolute; left: 0; right: 0; top: 378px; height: 130px; background: var(--ink);
  }
  .contact-labels {
    position: absolute; left: 29px; top: 14px; color: var(--gold-text);
    font-size: 25px; line-height: 38px;
  }
  .contact-divider {
    position: absolute; left: 121px; top: 18px; width: 2px; height: 72px; background: #444;
  }
  .contact-values {
    position: absolute; left: 137px; top: 12px; color: var(--gold-text);
    font-size: 27px; line-height: 39px;
  }
  .contact-values b { font-weight: 700; }
  .sales-box {
    position: absolute; left: 675px; top: 28px; width: 282px; height: 62px;
    border: 3px solid var(--gold-text); border-radius: 8px; color: var(--gold-text);
  }
  .sales-label {
    position: absolute; top: -18px; left: 38px; padding: 0 6px; background: var(--ink);
    font-size: 27px; line-height: 30px;
  }
  .sales-number {
    position: absolute; left: 12px; top: 14px; display: flex; align-items: center; gap: 8px;
    font-weight: 700; font-size: 29px; line-height: 32px;
  }
  .web-pill {
    position: absolute; left: 155px; top: 480px; width: 672px; height: 56px;
    background: linear-gradient(var(--sun), #f3c400);
    border-radius: 20px; border: 3px solid #2a1a00;
    display: flex; align-items: center; justify-content: center;
    color: var(--ink); font-size: 24px; letter-spacing: 5px;
  }
  .web-pill b { font-weight: 900; letter-spacing: 6px; }

  .diet-list {
    position: absolute; left: 361px; top: 205px; list-style: none;
    color: var(--gold-text); font-size: 29px; line-height: 38px;
  }
  .diet-list li::before { content: "•"; margin-right: 10px; }
  .natural-badge { position: absolute; left: 827px; top: 407px; }
</style>
</head>
<body>
  <section class="card card-front">
    <div class="sunset-scene" role="img" aria-label="Sunset savanna scene with a dog silhouette, acacia trees and grass against a large yellow sun"></div>
    <div class="brand-block"><span class="brand-name">Meadowlark Pet</span></div>
    <div class="tagline">100% NATURAL RAW DOG FOOD</div>
    <div class="holder">
      <div class="holder-name">Tom Browning</div>
      <div class="holder-title">Customer Experience Officer</div>
    </div>

    <div class="contact-band">
      <div class="contact-labels">Email<br>Direct</div>
      <div class="contact-divider"></div>
      <div class="contact-values">tbrowning@<b>meadowlarkpet</b>-example.com<br>(555) 123-4567</div>
      <div class="sales-box">
        <span class="sales-label">Sales Inquiries</span>
        <span class="sales-number">
          <svg width="16" height="26" viewBox="0 0 16 26" aria-hidden="true"><path d="M12 1 L6 1 Q1 3 1 13 Q1 23 6 25 L12 25 L12 19 L7 19 Q6 13 7 7 L12 7 Z" fill="currentColor"/></svg>
          (800) 555-0147
        </span>
      </div>
    </div>

    <div class="web-pill">www.<b>meadowlarkpet-example</b>.com</div>
  </section>

  <section class="card card-back">
    <ul class="diet-list">
      <li>Combination Diet</li>
      <li>Chicken Diet</li>
      <li>Beef Diet</li>
      <li>Lamb Diet</li>
    </ul>
    <svg class="natural-badge" width="124" height="124" viewBox="0 0 124 124" role="img" aria-label="Natural product badge">
      <circle cx="62" cy="62" r="58" fill="none" stroke="#f5d90a" stroke-width="4"/>
    </svg>
  </section>
</body>
</html>
```